Business Card Design Project

I am looking for a business card design for my custom Audio/Video & Contracting business named Brelvora Systems Inc. We do not currently have a corporate logo so you should not feel constrained to work around an existing design. Your design should be elegant and clean while artistically conveying that we are a technology company. We provide A/V services for the commercial and residential markets and contracting services for residential remodeling and home theater construction. We do not have a particular color that we are looking to design around so feel free to be creative.

To get references of the kind of work that we do and design inspiration please visit the following sites:

http://www.quenlamark.us
www.morvethpro.com
www.feltonbraxa.com

Reason: I think we are getting close on a couple of the designs and want to give additional time to get tweaks done and to resubmit your designs.

Target Market(s)

Most of our clients are very wealthy and have been exposed to premium brand names in every aspect of their lives, (ie. - luxury autos, estate sized homes, fine jewelery and clothes) and your design needs to convey that same level of excellent design that they are used to.

Industry/Entity Type

Residential

Requirements
Should not have
• An extensive use of the color RED.

```html
<!DOCTYPE html>
<html lang="en">
<head>
<meta charset="utf-8">
<title>Brelvora Systems – Business Cards</title>
<link rel="stylesheet" href="https://fonts.googleapis.com/css2?family=Courier+Prime&display=swap">
<style>
  :root {
    --page-bg: #f4efeb;
    --card-dark: #652703;
    --card-mid: #8a4a22;
    --card-light: #aa7250;
    --accent-orange: #e8601c;
    --accent-glow: #f07a3a;
    --frame-cream: #f6d6c2;
    --name-cream: #f3dccb;
    --name-peach: #f5c3a2;
    --photo-dark: #1c1816;
    --photo-mid: #4a4440;
    --grid-tone: #8e5230;
  }
  html, body {
    margin: 0;
    padding: 0;
    width: 1200px;
    height: 800px;
    overflow: hidden;
    background: var(--page-bg);
  }
  .canvas {
    position: relative;
    width: 1200px;
    height: 800px;
  }
  .card-art {
    display: block;
    width: 1200px;
    height: 800px;
  }
  .brand-name {
    font-family: "Courier Prime", "Courier New", monospace;
  }
</style>
</head>
<body>
<main class="canvas">
  <svg class="card-art" viewBox="0 0 1200 800" xmlns="http://www.w3.org/2000/svg">
    <defs>
      <linearGradient id="card-fill" x1="0" y1="0" x2="0" y2="1">
        <stop offset="0" stop-color="var(--card-dark)"/>
        <stop offset="0.45" stop-color="var(--card-mid)"/>
        <stop offset="1" stop-color="var(--card-light)"/>
      </linearGradient>
      <linearGradient id="glow-bar" x1="0" y1="0" x2="1" y2="0">
        <stop offset="0" stop-color="#c84a14"/>
        <stop offset="0.5" stop-color="var(--accent-glow)"/>
        <stop offset="1" stop-color="#b8420e"/>
      </linearGradient>
      <linearGradient id="camera-fill" x1="0" y1="0" x2="1" y2="1">
        <stop offset="0" stop-color="var(--photo-mid)"/>
        <stop offset="1" stop-color="var(--photo-dark)"/>
      </linearGradient>
      <filter id="card-shadow" x="-5%" y="-5%" width="110%" height="115%">
        <feDropShadow dx="0" dy="3" stdDeviation="4" flood-color="#3a1a08" flood-opacity="0.35"/>
      </filter>
    </defs>

    <!-- Front card -->
    <g class="card card--front">
      <rect class="card-face" x="16" y="16" width="712" height="396" rx="6" fill="url(#card-fill)" filter="url(#card-shadow)"/>
      <rect class="accent-glow-bar" x="28" y="26" width="238" height="36" fill="url(#glow-bar)" opacity="0.9"/>
      <rect class="accent-top-rule" x="266" y="24" width="452" height="5" fill="var(--accent-orange)"/>
      <rect class="accent-side-rule" x="710" y="24" width="7" height="274" fill="var(--accent-orange)"/>
      <polyline class="dotted-frame" points="28,70 273,70 273,40 704,40 704,296"
                fill="none" stroke="var(--accent-orange)" stroke-width="1.5" stroke-dasharray="3 3"/>
      <rect class="brand-mark" x="128" y="196" width="22" height="22" fill="var(--card-dark)" stroke="var(--name-cream)" stroke-width="1"/>
      <line class="name-rule" x1="197" y1="197" x2="548" y2="197"
            stroke="var(--accent-orange)" stroke-width="1.5" stroke-dasharray="3 3"/>
      <text class="brand-name brand-name--front" x="197" y="235" font-size="30" fill="var(--name-cream)">Brelvora Systems</text>
      <rect class="texture-patch" x="533" y="302" width="183" height="100" fill="var(--grid-tone)" opacity="0.55"
            role="img" aria-label="Fine square grid texture"/>
    </g>

    <!-- Back card -->
    <g class="card card--back">
      <rect class="card-face" x="555" y="437" width="628" height="349" rx="6" fill="url(#card-fill)" filter="url(#card-shadow)"/>
      <rect class="frame-rule frame-rule--top" x="566" y="449" width="607" height="6" fill="var(--frame-cream)"/>
      <rect class="frame-rule frame-rule--bottom" x="566" y="769" width="607" height="6" fill="var(--frame-cream)"/>
      <line class="frame-side frame-side--left" x1="567" y1="455" x2="567" y2="769"
            stroke="var(--frame-cream)" stroke-width="3" stroke-dasharray="8 6"/>
      <line class="frame-side frame-side--right" x1="1172" y1="455" x2="1172" y2="769"
            stroke="var(--frame-cream)" stroke-width="3" stroke-dasharray="8 6"/>
      <rect class="product-photo" x="755" y="488" width="220" height="172" rx="10" fill="url(#camera-fill)"
            role="img" aria-label="Photograph of a professional video camera"/>
      <text class="brand-name brand-name--back" x="872" y="714" font-size="50" text-anchor="middle"
            fill="var(--name-peach)" letter-spacing="1">BRELVORA SYSTEMS</text>
    </g>
  </svg>
</main>
</body>
</html>
```